Pinecrest Renovations - Get the creative juices going!!

Pinecrest does not do the actual renovation work. The company provides high end project management of renovation (primarily residential - with an eye toward commercial) The renovation work could look very different between projects. This company manages the work of contractors, architects and interior designers (either subcontracted directly by Pinecrest or hired by the client and entrusted to Pinecrest to manage). Clients are high end in the economic scale and the card needs to have a high end feel to it.

The owner is female, but the audience will be heavily slanted male. It should not be a "feminine" or "masculine" looking card. If anything, slant more on the masculine side. Clean, simple, yet creative and artistically appealing. The card design should complement and in no way compete with the logo.

When people think of our company: trust, integrity, dynamic, limitless possibilities, transition, energy, creative. We plan to expand in the future to be international.

There will also be a contest running for stationary. Please check that section, as well.

***Black is 80-90 percent black. Not stark black

Tight timeline. Needs cards printed quickly!

Residential

```html
<!DOCTYPE html>
<html lang="en">
<head>
<meta charset="utf-8">
<title>Pinecrest Renovations – Business Card</title>
<link rel="stylesheet" href="https://fonts.googleapis.com/css2?family=Lato:ital,wght@0,300;0,400;0,700;1,400&display=swap">
<style>
  :root {
    --backdrop: #5f5f5f;
    --paper: #f5f5f4;
    --ink: #333333;
    --ink-soft: #3f3f3f;
    --teal: #13a89e;
    --swoosh: #3a3a3a;
    --white: #ffffff;
  }

  * { box-sizing: border-box; margin: 0; padding: 0; }

  html, body {
    width: 1200px;
    height: 900px;
    overflow: hidden;
  }

  body {
    background: var(--backdrop);
    font-family: "Lato", "Helvetica Neue", Arial, sans-serif;
    display: flex;
    align-items: center;
    justify-content: center;
  }

  .business-card {
    position: relative;
    width: 1000px;
    height: 572px;
    background: var(--paper);
    overflow: hidden;
    box-shadow: 0 18px 40px rgba(0, 0, 0, 0.35);
  }

  .card-bands {
    position: absolute;
    inset: 0;
    width: 1000px;
    height: 572px;
  }

  .swoosh { fill: var(--swoosh); }
  .band { fill: var(--teal); }

  .brand {
    position: absolute;
    left: 58px;
    top: 42px;
  }

  .brand-square {
    width: 50px;
    height: 50px;
    background: var(--teal);
    margin-left: 120px;
    margin-bottom: 24px;
  }

  .brand-name {
    font-weight: 700;
    font-size: 28px;
    letter-spacing: 1.5px;
    color: var(--ink);
    text-transform: uppercase;
    line-height: 1;
  }

  .person {
    position: absolute;
    left: 58px;
    top: 180px;
  }

  .person-name {
    font-weight: 400;
    font-size: 46px;
    letter-spacing: 1px;
    color: var(--ink-soft);
    line-height: 1;
    text-transform: uppercase;
  }

  .person-title {
    margin-top: 10px;
    font-weight: 700;
    font-size: 25px;
    color: var(--teal);
    line-height: 1;
  }

  .contact-list {
    position: absolute;
    left: 58px;
    top: 280px;
    list-style: none;
    font-size: 22px;
    color: var(--ink);
    line-height: 34px;
  }

  .contact-label { font-style: italic; }

  .address {
    position: absolute;
    left: 58px;
    bottom: 38px;
    font-weight: 700;
    font-size: 24px;
    letter-spacing: 0.6px;
    color: var(--white);
  }
</style>
</head>
<body>
  <article class="business-card">
    <svg class="card-bands" viewBox="0 0 1000 572" aria-hidden="true">
      <path class="swoosh" d="M0,438 C300,432 560,404 770,356 C870,334 945,324 1000,326 L1000,346 C935,346 850,362 740,390 C530,440 280,462 0,468 Z"/>
      <path class="band" d="M0,478 C280,472 540,448 750,402 C860,378 945,362 1000,362 L1000,572 L0,572 Z"/>
    </svg>

    <header class="brand">
      <div class="brand-square"></div>
      <p class="brand-name">Pinecrest Renovations</p>
    </header>

    <section class="person">
      <h1 class="person-name">Your Name</h1>
      <p class="person-title">Title text</p>
    </section>

    <ul class="contact-list">
      <li><span class="contact-label">phone</span>: 123-456-7890</li>
      <li><span class="contact-label">web</span>: yourdomain.com</li>
      <li><span class="contact-label">email</span>: yourname@yourdomain.com</li>
    </ul>

    <p class="address">Street address goes here, Suite #303, Alt Bldg, NY 82365</p>
  </article>
</body>
</html>
```